Building and Maintenance Company requires a flyer design, Specialising in domestic and commercial bu

We need a flyer design for a company based in Melbourne Victoria, we want to send the flyer out to businesses to obtain more work.

KEV Building and Construction provides the solution for all your building and maintenance needs

We have a professional and highly regarded team of reliable and skilled tradesmen who specialise in building services, domestic and commercial maintenance and gardening in Victoria and Tasmania.

Include our contact details;
0412 738 206
info@kevbuilding.example.au
www.kevbuilding.example.au

Target Market(s)

Domestic and Commercial Clients looking for building maintenance, window cleaning or gardening

Industry/Entity Type

It Company

Font styles to use
Sans Serif

Colors
33b8a4
474747
ffffff

Requirements
Must have
• Images and colour
Nice to have
• We would like the flyer to have our contact details on it.
• Colourful
• Clearly explains what we do, which is, 'KEV Building and Construction provides the solution for all your building, maintenance and gardening needs.'

```html
<!DOCTYPE html>
<html lang="en">
<head>
<meta charset="utf-8">
<title>KEV Building and Construction – Flyer</title>
<link href="https://fonts.googleapis.com/css2?family=Encode+Sans+Condensed:wght@400;600&family=Lato:wght@300;400&family=Open+Sans:wght@700&family=Roboto:wght@400&display=swap" rel="stylesheet">
<style>
  :root {
    --teal: #33b8a4;
    --charcoal: #474747;
    --white: #ffffff;
    --panel: #f2f2f2;
    --ink: #3a3a3a;
    --backdrop: #e6e6e6;
  }
  * { margin: 0; padding: 0; box-sizing: border-box; }
  html, body { width: 1041px; height: 1200px; overflow: hidden; background: var(--backdrop); }
  .flyer {
    position: absolute; left: 107px; top: 15px;
    width: 826px; height: 1170px;
    background: var(--panel);
    overflow: hidden;
    box-shadow: 0 2px 10px rgba(0,0,0,.18);
  }
  .hero {
    position: absolute; left: 0; top: 0; width: 826px; height: 516px;
    background: linear-gradient(135deg, #8a6a4c 0%, #b58f67 35%, #6e5640 65%, #3f3128 100%);
  }
  .brand-panel { position: absolute; left: 0; top: 0; }
  .brand-name {
    position: absolute; left: 50px; top: 48px; width: 240px;
    font-family: "Encode Sans Condensed", sans-serif; font-weight: 600;
    color: var(--charcoal); text-transform: uppercase;
    font-size: 27px; line-height: 34px; letter-spacing: 2px;
  }
  .tagline-band {
    position: absolute; left: 0; top: 516px; width: 826px; height: 118px;
    background: var(--charcoal); color: var(--white);
    display: flex; align-items: center; justify-content: center; text-align: center;
    font-family: "Encode Sans Condensed", sans-serif; font-weight: 400;
    font-size: 25px; line-height: 36px; text-transform: uppercase;
    padding: 0 20px;
  }
  .specialising { position: absolute; left: 41px; top: 680px; width: 740px; }
  .specialising h2 {
    font-family: "Open Sans", sans-serif; font-weight: 700; font-size: 20px;
    color: var(--ink); letter-spacing: .2px; line-height: 26px;
  }
  .specialising h2 span { color: var(--teal); }
  .specialising p {
    font-family: "Lato", sans-serif; font-weight: 300; font-size: 19.5px;
    line-height: 26.5px; color: #222;
  }
  .service-strip {
    position: absolute; left: 58px; top: 821px; width: 703px; height: 187px;
    background: linear-gradient(90deg, #4f7a3a 0%, #c9c9c4 30%, #cfd0cc 45%, #6a6f78 60%, #3d7a2c 80%, #57a03c 100%);
  }
  .web-tab { position: absolute; left: 0; top: 1087px; }
  .web-address {
    position: absolute; left: 30px; top: 1097px;
    font-family: "Open Sans", sans-serif; font-weight: 700; font-size: 19px;
    color: var(--white); white-space: nowrap;
  }
  .contact-bar {
    position: absolute; left: 0; top: 1101px; width: 826px; height: 69px;
    background: var(--charcoal);
  }
  .contact {
    position: absolute; top: 1122px; display: flex; align-items: center; gap: 9px;
    font-family: "Roboto", sans-serif; font-size: 18px; color: var(--white);
    white-space: nowrap;
  }
  .contact.phone { left: 360px; }
  .contact.email { left: 532px; gap: 6px; }
  .contact svg { display: block; }
</style>
</head>
<body>
<main class="flyer">
  <div class="hero" role="img" aria-label="Photo of a carpenter's hands marking timber with a pencil beside a hammer, chisels and wood shavings on a workbench"></div>

  <svg class="brand-panel" width="380" height="210" viewBox="0 0 380 210" aria-hidden="true">
    <polygon points="0,0 373,0 280,203 0,203" fill="var(--white)"/>
  </svg>
  <div class="brand-name">KEV Building and Construction</div>

  <div class="tagline-band">KEV Building and Construction provides the solution for all your<br>building, maintenance and gardening needs</div>

  <section class="specialising">
    <h2>SPECIALISING <span>IN</span></h2>
    <p>domestic and commercial building maintenance, services and garden maintenance, we provide accurate knowledge and maintain a professional relationship in order to achieve high quality results.</p>
  </section>

  <div class="service-strip" role="img" aria-label="Strip of service photos: hedge trimming, painting a wall with a roller, a tradesman with a cordless drill and tool belt, and garden shears pruning a shrub"></div>

  <div class="contact-bar"></div>
  <svg class="web-tab" width="370" height="47" viewBox="0 0 370 47" aria-hidden="true">
    <polygon points="0,0 362,0 327,47 0,47" fill="var(--teal)"/>
  </svg>
  <div class="web-address">www.kevbuilding.example.au</div>

  <div class="contact phone">
    <svg width="18" height="18" viewBox="0 0 18 18" aria-hidden="true">
      <circle cx="9" cy="9" r="9" fill="var(--white)"/>
      <path d="M6.2 4.3 L7.6 6.3 L6.8 7.4 C7.4 8.8 8.7 10.1 10.1 10.7 L11.2 9.9 L13.2 11.3 L12.4 13 C9 13 4.8 8.8 4.6 5.1 Z" fill="var(--charcoal)"/>
    </svg>
    <span>0412 738 206</span>
  </div>
  <div class="contact email">
    <svg width="19" height="19" viewBox="0 0 19 19" aria-hidden="true">
      <circle cx="9.5" cy="9.5" r="9.5" fill="var(--white)"/>
      <rect x="4.5" y="6" width="10" height="7" fill="none" stroke="var(--charcoal)" stroke-width="1.3"/>
      <path d="M4.5 6 L9.5 10 L14.5 6" fill="none" stroke="var(--charcoal)" stroke-width="1.3"/>
    </svg>
    <span>info@kevbuilding.example.au</span>
  </div>
</main>
</body>
</html>
```